Bramble Harbor Foundation Web Design

The design we need is for a WordPress blog that will be our content platform. We are a registered 501(c)3 non-profit that focuses on financially supporting the treatment of cancer patients that have been told they have no hope and there is nothing the conventional medical system can do for them. Through this wesbite we want to both rasie awareness about the treatment options plus, raise funds for treating patients. The two primary target audiences of the site are...

1. Terminally ill patients and their families to let them know that there is an option other then hospice and that we are hear to support that option.

2. People looking to help donate to a worthwhile cause that resonates with them.

The website is https://brambleharborfoundation.org/

See attached logo designs!!!

Target Market(s)

Cancer patients and their families

Industry/Entity Type

Foundation

Font styles to use
Sans Serif

Colors
ffffff
fbed22

Requirements
Must have
• I like this look of this site. It is clean, simple, helpful, soft. I like the flow of the pages.
• http://www.quietmeadowtrust.org/
• I like the design and flow but NOT the color or boldness
• https://tmvq-youth.org/
• I like this style for a donation page.
• https://www.curewaveaid.org/about-cwa/stand-with-us/gifts/single-gift
• with the addition of a Would you like your employer to match? button.
Nice to have
• White black and gold - but soft
• Even possibly grayscale like the site I like.

```html
<!DOCTYPE html>
<html lang="en">
<head>
<meta charset="utf-8">
<title>Bramble Harbor Foundation</title>
<link rel="stylesheet" href="https://fonts.googleapis.com/css2?family=Aleo:wght@300;400;700&family=Lato:wght@400&display=swap">
<style>
  :root {
    --gold: #ebc95a;
    --ink: #1c1c1c;
    --muted: #8d8d8d;
    --grey: #e8e8e8;
    --rule: #d6d6d6;
    --paper: #ffffff;
  }
  * { margin: 0; padding: 0; box-sizing: border-box; }
  html, body { width: 683px; height: 1200px; overflow: hidden; background: var(--paper); }
  body { position: relative; font-family: "Aleo", Georgia, serif; color: var(--ink); }
  .abs { position: absolute; }

  .brand { left: 76px; top: 42px; display: flex; align-items: center; gap: 6px; }
  .brand-mark { width: 10px; height: 10px; background: var(--gold); }
  .brand-name { font-family: "Aleo", serif; font-weight: 700; font-size: 10px; color: var(--ink); letter-spacing: 0.2px; }

  .nav { right: 84px; top: 47px; display: flex; gap: 11px; font-family: "Lato", sans-serif; font-size: 7px; letter-spacing: 1px; color: #666; }
  .nav a { color: inherit; text-decoration: none; padding: 0 2px 5px; }
  .nav a.is-active { color: var(--gold); border-bottom: 1px solid var(--gold); }

  .hero-side { left: 0; top: 117px; width: 183px; height: 264px; background: var(--grey); }
  .hero-photo { left: 198px; top: 105px; width: 485px; height: 263px;
    background: radial-gradient(ellipse 55% 45% at 58% 55%, #e6c0a5 0%, #dcc4b4 45%, rgba(226,226,230,0) 80%), #e3e3e7; }
  .hero-accent { left: 0; top: 0; }
  .hero-band { left: 0; top: 244px; width: 353px; height: 37px; background: var(--paper); }
  .hero-band-low { left: 0; top: 281px; width: 333px; height: 33px; background: var(--paper); }
  .hero-title { left: 221px; top: 244px; font-weight: 300; font-size: 29px; line-height: 33px; color: var(--ink); }
  .hero-title .accent { color: var(--gold); font-weight: 700; }
  .hero-sub { left: 221px; top: 319px; font-weight: 300; font-size: 8.5px; line-height: 11.5px; color: var(--muted); }

  .help-head { left: 0; top: 414px; width: 184px; height: 31px; background: var(--gold); color: #fff;
    font-family: "Lato", sans-serif; font-size: 8.5px; letter-spacing: 1.8px; text-align: center; line-height: 31px; padding-left: 44px; }
  .help-text { left: 56px; top: 456px; width: 116px; font-size: 6.6px; line-height: 10.5px; }
  .donate { left: 59px; top: 547px; width: 102px; height: 24px; border: 1px solid var(--gold); border-radius: 5px;
    color: var(--gold); font-family: "Lato", sans-serif; font-size: 6.8px; letter-spacing: 1.6px; text-align: center; line-height: 22px; }
  .help-frame { left: 0; top: 0; }
  .mission { left: 218px; top: 431px; width: 380px; font-weight: 300; font-size: 18.5px; line-height: 22.5px; color: #9a9a9a; }

  .post-photo { width: 108px; height: 86px;
    background: linear-gradient(180deg, #b9c9d2 0%, #cfc4ab 45%, #b59a6a 100%); }
  .post-title { width: 340px; font-size: 15px; line-height: 19px; font-weight: 400; }
  .post-rule { width: 364px; height: 1px; background: var(--rule); }
  .post-date { font-family: "Lato", sans-serif; font-size: 5px; letter-spacing: 0.6px; color: var(--muted); }
  .post-body { width: 362px; font-size: 6.4px; line-height: 10.6px; }
  .post-body p + p { margin-top: 10.6px; }

  .footer-rule { left: 58px; top: 1097px; width: 547px; height: 1px; background: var(--rule); }
  .footer-copy { left: 65px; top: 1102px; font-size: 5px; }
</style>
</head>
<body>

<header>
  <div class="abs brand"><span class="brand-mark"></span><span class="brand-name">Bramble Harbor Foundation</span></div>
  <nav class="abs nav"><a class="is-active" href="#">HOME</a><a href="#">ABOUT US</a><a href="#">CONTACT</a></nav>
</header>

<section class="hero">
  <div class="abs hero-side"></div>
  <div class="abs hero-photo" role="img" aria-label="Photo of two hands gently holding each other on a pale grey background"></div>
  <svg class="abs hero-accent" width="683" height="400" aria-hidden="true">
    <polygon points="183,117 198,105 198,368 183,381" fill="var(--gold)"/>
  </svg>
  <div class="abs hero-band"></div>
  <div class="abs hero-band-low"></div>
  <h1 class="abs hero-title"><span class="accent">help</span> save<br>the lives</h1>
  <p class="abs hero-sub">of all those that have been diagnosed<br>with terminal cancer and have no where else turn</p>
</section>

<section class="help">
  <svg class="abs help-frame" width="683" height="600" aria-hidden="true">
    <path d="M184.5 445 V587.5 H623" fill="none" stroke="var(--gold)" stroke-width="1"/>
  </svg>
  <div class="abs help-head">HELP US</div>
  <p class="abs help-text">Lorem ipsum dolor sit amet, consectetur adipiscing elit. Ut ex est, congue nec placerat vel, molestie in metus. Integer facilisis quis lectus quis sollicitudin. Integer euismod iaculis odio, ut tempor dolor lacinia id.</p>
  <div class="abs donate">DONATE</div>
  <p class="abs mission">We are a registered 501(c)3 non-profit that focuses on financially supporting the research and treatment of cancer patients that have been told they have no hope and there is nothing the conventional medical system can do for them.</p>
</section>

<article class="post">
  <div class="abs post-photo" style="left:58px;top:660px" role="img" aria-label="Photo of a hand brushing through golden wheat"></div>
  <h2 class="abs post-title" style="left:218px;top:661px">New “Bramble Harbor Foundation” Website Coming Soon!</h2>
  <div class="abs post-rule" style="left:218px;top:704px"></div>
  <div class="abs post-date" style="left:221px;top:710px">NOVEMBER 1, 2017</div>
  <div class="abs post-body" style="left:221px;top:731px">
    <p>We are a registered 501(c)3 non-profit that focuses on financially supporting the research and treatment of cancer patients that have been told they have no hope and there is nothing the conventional medical system can do for them.</p>
    <p>If you would like to contact us about the great foundation and how you can work with us to help save the lives of all those that have been diagnosed with terminal cancer and have no where else turn, please contact us by clicking here.</p>
  </div>
</article>

<article class="post">
  <div class="abs post-photo" style="left:58px;top:869px" role="img" aria-label="Photo of a hand brushing through golden wheat"></div>
  <h2 class="abs post-title" style="left:218px;top:870px">New “Bramble Harbor Foundation” Website Coming Soon!</h2>
  <div class="abs post-rule" style="left:218px;top:913px"></div>
  <div class="abs post-date" style="left:221px;top:919px">NOVEMBER 1, 2017</div>
  <div class="abs post-body" style="left:221px;top:940px">
    <p>We are a registered 501(c)3 non-profit that focuses on financially supporting the research and treatment of cancer patients that have been told they have no hope and there is nothing the conventional medical system can do for them.</p>
    <p>If you would like to contact us about the great foundation and how you can work with us to help save the lives of all those that have been diagnosed with terminal cancer and have no where else turn, please contact us by clicking here.</p>
  </div>
</article>

<footer>
  <div class="abs footer-rule"></div>
  <p class="abs footer-copy">© Bramble Harbor Foundation</p>
</footer>

</body>
</html>
```